Kindle Thread Pty Ltd Brochure and New Image Design

Initally we will be needing a A4 Folder design created as well as a Template for a Double Sided Flyer. We need a cutting edge design which we can incorporate into a Brochure, Flyer Handout, Website etc. Basically we are re-branding our company starting with an "About Us" Folder which we will be distributing to potential customers.
We are an Embroidery company that caters for mid-large companies dealing with clothing ranging from Corporate Attire to Workwear. Our current website has more information on what we do and you can use that as a valid reference point (www.kindlethread.com.au), However the website will be step 2 in freshening up our image.
Our company has been thriving over the 20 years we have been in business by supplying a higher quality product as well as Service that is second to none, unfortunately our branding image has been overlooked while we have spent more time/effort on our customer service.
We have used the colours Maroon (PMS 216C) Silver Grey (PMS Cool Gray 7) White and Black. We would like to maintain these colours but incorporate them together in a way that has a more "modern edgey" look.
Target Market(s)
Purchasing / Marketing Officers of Mid-Large Corporate Companies.
Industry/Entity Type
Clothing
Look and feel

```html
<!DOCTYPE html>
<html lang="en">
<head>
<meta charset="utf-8">
<title>Kindle Thread – A4 Folder Cover</title>
<link rel="stylesheet" href="https://fonts.googleapis.com/css2?family=Cabin:wght@500;600&display=swap">
<style>
  :root {
    --maroon: #8b0a44;
    --maroon-deep: #7a0a3c;
    --band-edge: #8d2a5c;
    --band-glow: #dcc6da;
    --silver-top: #c8c9cb;
    --silver-mid: #e6e6e7;
    --paper: #fbfbfb;
    --stage: #ffffff;
    --white: #ffffff;
  }
  * { margin: 0; padding: 0; box-sizing: border-box; }
  html, body {
    width: 1200px;
    height: 900px;
    overflow: hidden;
    background: var(--stage);
  }
  .folder-cover {
    position: absolute;
    left: 100px;
    top: 110px;
    width: 1000px;
    height: 680px;
    overflow: hidden;
    background: linear-gradient(180deg, var(--silver-top) 0%, var(--silver-mid) 40%, var(--paper) 75%, var(--white) 100%);
    font-family: "Cabin", sans-serif;
  }
  .folder-cover p { line-height: 1; white-space: nowrap; }
  .wave-pattern {
    position: absolute;
    inset: 0;
    background:
      radial-gradient(ellipse 260px 420px at 560px 250px, rgba(150,150,155,0.10), transparent 70%),
      radial-gradient(ellipse 200px 320px at 860px 520px, rgba(150,150,155,0.09), transparent 70%),
      radial-gradient(ellipse 300px 140px at 250px 420px, rgba(150,150,155,0.08), transparent 70%);
  }
  .brand-band {
    position: absolute;
    left: 0;
    top: 255px;
    width: 490px;
    height: 150px;
    background: linear-gradient(90deg, var(--band-edge) 0%, #b98aab 25%, var(--band-glow) 48%, #b07a9b 78%, var(--maroon-deep) 100%);
  }
  .accent-band {
    position: absolute;
    left: 490px;
    top: 255px;
    width: 472px;
    height: 131px;
    background: var(--maroon);
  }
  .range-photo {
    position: absolute;
    left: 490px;
    top: 165px;
    width: 407px;
    height: 187px;
    background: linear-gradient(90deg, #b9a58e 0%, #d8cdc2 30%, #c9b7a6 55%, #8f9092 78%, #a7a8aa 100%);
  }
  .company-name {
    position: absolute;
    left: 723px;
    top: 359px;
    font-size: 19px;
    font-weight: 600;
    color: var(--white);
    letter-spacing: 0.2px;
  }
  .service-line {
    position: absolute;
    left: 826px;
    top: 392px;
    font-size: 15px;
    font-weight: 600;
    color: var(--maroon);
    letter-spacing: 0.3px;
  }
  .brand-mark {
    position: absolute;
    font-size: 22px;
    font-weight: 600;
    color: var(--maroon);
  }
  .brand-mark--band {
    left: 177px;
    top: 319px;
  }
  .brand-mark--corner {
    right: 38px;
    top: 605px;
  }
</style>
</head>
<body>
  <main class="folder-cover">
    <div class="wave-pattern" role="img" aria-label="Fine flowing grey line waves across the cover"></div>
    <div class="accent-band"></div>
    <div class="brand-band"></div>
    <div class="range-photo" role="img" aria-label="Photo of models wearing corporate attire: dresses, suits and blazers"></div>
    <p class="company-name">Kindle Thread</p>
    <p class="service-line">Embroidery</p>
    <p class="brand-mark brand-mark--band">Kindle Thread</p>
    <p class="brand-mark brand-mark--corner">Kindle Thread</p>
  </main>
</body>
</html>
```